Corporate Branding - Web and Print

A UK based company will like to use an existing logo to create branding materials for all marketing related documents, including business card, prints, letterhead, Website, Twitter, Facebook, Instagram logo etc. This company serves high-end clientele in the fashion, health and wellness and as such high quality and class is of utmost importance.
Where the logo can be modernised without losing its character then experiment. The main thing is to have a corporate branding which can be used later for brochures, Business Plan infographics.
The prominent colour within the organisation is burnt orange with no secondary colour. However if you believe a secondary colour is needed then use it, otherwise keep it simple and classy. Any chosen colours have to match perfectly.
Target Market(s)
High net worth individuals
Industry/Entity Type
Health And Wellness
Contact Information for Business Card
classy
Look and feel
Each slider illustrates characteristics of the customer's brand and the style your logo design should communicate.

```html
<!DOCTYPE html>
<html lang="en">
<head>
<meta charset="utf-8">
<title>Velmora Business Card</title>
<link href="https://fonts.googleapis.com/css2?family=Roboto:wght@400;700;900&display=swap" rel="stylesheet">
<style>
  :root {
    --brand-orange: #f7931e;
    --panel-orange: #f59322;
    --bg-top: #f7951f;
    --bg-bottom: #ff8500;
    --card-white: #ffffff;
    --ink: #333333;
  }
  * { margin: 0; padding: 0; box-sizing: border-box; }
  html, body { width: 1200px; height: 1200px; overflow: hidden; }
  body {
    background: linear-gradient(180deg, var(--bg-top), var(--bg-bottom));
    font-family: "Roboto", Arial, sans-serif;
    position: relative;
  }
  .card {
    position: absolute;
    left: 303px;
    width: 594px;
    height: 339px;
    background: var(--card-white);
    border-radius: 19px;
    box-shadow: 0 14px 22px rgba(120, 60, 0, 0.35);
    overflow: hidden;
  }
  .card--front { top: 194px; }
  .card--back { top: 669px; }

  .brand-mark {
    position: absolute;
    border-radius: 50%;
    background: var(--brand-orange);
  }
  .card--front .brand-mark { width: 104px; height: 104px; left: 243px; top: 74px; }
  .brand-name {
    position: absolute;
    left: 0; right: 0;
    text-align: center;
    font-weight: 900;
    color: var(--brand-orange);
    letter-spacing: 2px;
    line-height: 1;
  }
  .card--front .brand-name { top: 186px; font-size: 64px; }

  .logo-panel {
    position: absolute;
    left: 0; top: 54px;
    width: 298px; height: 136px;
    background: var(--panel-orange);
    border-radius: 0 16px 16px 0;
  }
  .logo-panel .brand-mark {
    width: 60px; height: 60px; left: 121px; top: 22px;
    background: var(--card-white);
  }
  .logo-panel .brand-name {
    top: 86px; font-size: 36px; color: var(--card-white); letter-spacing: 1px;
  }

  .holder {
    position: absolute; right: 29px; top: 96px; text-align: right;
    color: var(--brand-orange);
  }
  .holder__name { font-size: 31px; font-weight: 700; letter-spacing: 1px; line-height: 1.1; }
  .holder__title { font-size: 14px; font-weight: 400; margin-top: 4px; }

  .contact-list { position: absolute; list-style: none; }
  .contact-list li {
    display: flex; align-items: center; gap: 8px;
    height: 26px; margin-bottom: 6px;
    font-size: 15px; color: var(--ink);
  }
  .contact-list--company { left: 24px; top: 212px; }
  .contact-list--personal { right: 23px; top: 228px; }
  .contact-list--personal li { justify-content: flex-end; margin-bottom: 5px; font-size: 16px; }
  .icon {
    width: 26px; height: 26px; flex: none;
    border-radius: 50%;
    background: var(--brand-orange);
    display: flex; align-items: center; justify-content: center;
  }
  .icon svg { width: 16px; height: 16px; }
</style>
</head>
<body>

<section class="card card--front" aria-label="Card front">
  <div class="brand-mark"></div>
  <div class="brand-name">VELMORA</div>
</section>

<section class="card card--back" aria-label="Card back">
  <div class="logo-panel">
    <div class="brand-mark"></div>
    <div class="brand-name">VELMORA</div>
  </div>

  <div class="holder">
    <div class="holder__name">ADRIAN COLE</div>
    <div class="holder__title">GENERAL MANAGER</div>
  </div>

  <ul class="contact-list contact-list--company">
    <li><span class="icon"></span>@velmoraApp</li>
    <li><span class="icon">
      <svg viewBox="0 0 16 16" fill="none" stroke="#fff" stroke-width="1.2"><rect x="2" y="4" width="12" height="8" rx="1"/><path d="M2 4l6 5 6-5"/></svg>
    </span>info@velmora.com</li>
    <li><span class="icon">
      <svg viewBox="0 0 16 16" fill="none" stroke="#fff" stroke-width="1"><circle cx="8" cy="8" r="6"/><ellipse cx="8" cy="8" rx="2.6" ry="6"/><path d="M2 8h12M3 5h10M3 11h10"/></svg>
    </span>www.velmora.com</li>
  </ul>

  <ul class="contact-list contact-list--personal">
    <li>+11 222333444<span class="icon">
      <svg viewBox="0 0 16 16" fill="#fff"><path d="M4.5 2l2 3-1.2 1.3c.7 1.6 1.9 2.8 3.4 3.5L10 8.6l3 2-1 2.4c-4.6.2-9-4.3-8.9-8.9z"/></svg>
    </span></li>
    <li>a.cole@velmora.com<span class="icon">
      <svg viewBox="0 0 16 16" fill="none" stroke="#fff" stroke-width="1.2"><rect x="2" y="4" width="12" height="8" rx="1"/><path d="M2 4l6 5 6-5"/></svg>
    </span></li>
  </ul>
</section>

</body>
</html>
```